依頼概要
■依頼の目的・概要
神奈川県の歯科医院です。
この度、地域の方々に当院を改めて知って頂きたく、
DMを作成し、ポスティングをする運びとなりました。
当院紹介のポスティング用DMの作成をお願いします。

■依頼詳細
枚数:未定
サイズ:B5またはA4

■今回のDMに記載して頂きたい事柄
①マザーズデーがあること
②近隣の保育園、小学校、中学校の学校認定医であること
③院長の写真、医院の写真
(準備出来次第すぐにアップロード致します。)
④無針注射を用いる等、痛みが軽減するよう努力していること

以上の4点は必ず記載してください。

■その他
●当院のホームページを記載しておきます。
https://www.kusunohama-dc.jp
当院のイメージやカラーはホームページを参考にしてください。
●当院は子どもの患者様が非常に多く、
親しみやすく通いやすい雰囲気づくりを心がけています。

以上を参考に作成していただけると嬉しいです。
JPEG・PPT・PNGフォーマットで製作お願いいたします。
全くの素人でして、あまりよく分かっていないのが現状です。
すみませんがよろしくお願いいたします。
■今回のDMに記載してほしい事柄
に追加です。
⑤産後健診も受付中で、相模原市乳幼児健診担当医在中であること。

以上⑤も必ず記載して頂きたい事柄に追加いたします。
よろしくお願いいたします。
院長の写真が用意できましたので、アップロード致します。
この写真を使用して下さい。
また、歯科医院の外観や内観等、必要な写真は
ホームページの写真を使用して下さい。
よろしくお願い致します。
外観、内観の写真もアップロード致します。
必要に応じて切り取り等して、使用してください。
よろしくお願い致します。
何度も追記してすみません。
写真をアップロード致します。
よろしくお願い致します。
マザーズデーは現在、月火金曜日の9:00-12:00に行っています。
締め切り一週間前に追記してしまいすみません。
ホームページに載っている
「楠ヶ浜台歯科クリニック」のロゴについてです。
この度当院の名前を新しくし、「ヶ」を「が」とし、
「楠が浜台歯科クリニック」と変更いたしました。
ロゴは今回追記する画像を使用してくださるようお願いいたします。
また、外観の写真ですが、古いままのロゴになってしまっているので
使用せずに作成お願いいたします。
尚、院長の写っている写真の背景が古いロゴのままになってしまっていますが、
これは細かい部分になるので、使用していただいて構いません。
要望が多くて申し訳ございません。よろしくお願いいたします。
分からない点などありましたら質問、メッセージ等ください。
よろしくお願いいたします。

シンプルで分かりやすく、必要最低限の内容が記載されており
とても見やすかったのと、当院のイメージカラーが
多く使われており、とても良いと思ったため
決定させて頂きました。

今回は皆さん素敵な提案をありがとうございました。
追記、コメントにも迅速に対応してくださる方が多く、
とても助かりました。お時間いただきありがとうございました。
機会がありましたら、またよろしくお願いいたします。

```html
<!DOCTYPE html>
<html lang="ja">
<head>
<meta charset="utf-8">
<title>楠が浜台歯科クリニック DM</title>
<link rel="stylesheet" href="https://fonts.googleapis.com/css2?family=M+PLUS+Rounded+1c:wght@500;700;800&family=Noto+Sans+JP:wght@400;500;700&display=swap">
<style>
:root{
  --green:#1f9a6f;
  --green-dark:#16785a;
  --leaf:#8cc63f;
  --pale:#e9f3cf;
  --cream:#fffbe8;
  --yellow:#fff3a8;
  --red:#d9362b;
  --orange:#f39800;
  --ink:#3a3a3a;
  --white:#ffffff;
}
*{box-sizing:border-box;margin:0;padding:0}
html,body{width:831px;height:1200px;overflow:hidden;background:var(--white)}
body{font-family:"Noto Sans JP",sans-serif;color:var(--ink)}
.sheet{position:relative;width:831px;height:1200px;overflow:hidden;background:var(--white)}
.top-banner{position:absolute;left:0;top:0;width:831px;height:88px;background:var(--green);color:var(--white);
  font-family:"M PLUS Rounded 1c",sans-serif;font-weight:700;font-size:25px;line-height:36px;text-align:center;padding-top:8px;letter-spacing:1px}
.brand{position:absolute;left:0;top:100px;width:831px;height:330px}
.brand-mark{position:absolute;left:335px;top:10px;width:160px;height:160px;border-radius:50%;background:var(--green);opacity:.9}
.brand-name{position:absolute;left:0;top:190px;width:831px;text-align:center;font-family:"M PLUS Rounded 1c",sans-serif;
  font-weight:800;font-size:50px;color:var(--green);letter-spacing:2px}
.brand-en{position:absolute;left:0;top:258px;width:831px;text-align:center;font-family:"M PLUS Rounded 1c",sans-serif;
  font-weight:700;font-size:24px;color:var(--green);letter-spacing:1px}
.cert{position:absolute;left:645px;top:36px;width:150px;height:160px}
.cert-label{position:absolute;left:0;top:0;width:150px;background:var(--yellow);border:3px solid var(--green);
  color:var(--green-dark);font-weight:700;font-size:19px;line-height:28px;text-align:center;padding:8px 0}
.cert-seal{position:absolute;left:49px;top:106px;width:52px;height:52px;border-radius:50%;background:var(--red)}
.lower{position:absolute;left:0;top:430px;width:831px;height:720px;background:var(--pale)}
.card{position:absolute;top:18px;width:390px;height:330px;background:var(--cream);border:3px solid var(--leaf);border-radius:18px;padding:18px 20px}
.card.mothers{left:18px}
.card.painless{left:423px;height:200px}
.card h2{font-family:"M PLUS Rounded 1c",sans-serif;font-weight:800;font-size:25px;line-height:32px;color:var(--green-dark);padding-left:66px;min-height:66px}
.card .icon{position:absolute;left:18px;top:18px;width:56px;height:56px;border-radius:50%;background:var(--orange)}
.card p{font-size:14px;line-height:22px;margin-top:8px}
.days{margin-top:12px;text-align:center}
.days small{display:inline-block;background:var(--green);color:var(--white);font-size:13px;padding:1px 14px;border-radius:10px}
.days strong{display:block;font-family:"M PLUS Rounded 1c",sans-serif;font-size:28px;color:var(--green-dark);margin-top:4px}
.postnatal{position:absolute;left:423px;top:232px;width:390px;text-align:center}
.postnatal .lead{display:inline-block;background:var(--yellow);color:var(--red);font-weight:700;font-size:24px;padding:2px 18px;border-radius:6px}
.postnatal .sub{margin-top:6px;font-weight:700;font-size:18px;color:var(--green-dark)}
.director-photo{position:absolute;left:460px;top:310px;width:330px;height:410px;background:linear-gradient(#d7e9d8,#7fb79a)}
.director-caption{position:absolute;left:640px;top:678px;background:var(--white);padding:2px 12px;font-size:17px;font-weight:700;color:var(--ink)}
.hours{position:absolute;left:18px;top:368px;width:420px;border-collapse:collapse;background:var(--white);font-size:17px}
.hours th,.hours td{border:1px solid #bcd59a;height:52px;text-align:center;font-weight:700}
.hours thead th{background:var(--green);color:var(--white);font-family:"M PLUS Rounded 1c",sans-serif;font-size:20px}
.hours tbody th{font-size:12px;width:84px;color:var(--green-dark);font-weight:500}
.hours td{color:var(--green-dark);font-size:20px}
.hours-note{position:absolute;left:18px;top:545px;width:430px;font-size:13px;line-height:20px}
.footer{position:absolute;left:0;top:1150px;width:831px;height:50px;background:var(--green);color:var(--white);display:flex;align-items:center;padding:0 18px;gap:14px}
.footer .tel{display:flex;align-items:center;gap:6px;font-family:"M PLUS Rounded 1c",sans-serif;font-weight:800;font-size:26px}
.footer .note{font-size:11px;line-height:15px;width:180px}
.footer .web{display:flex;align-items:center;gap:6px;font-size:19px;font-weight:500;margin-left:auto}
</style>
</head>
<body>
<div class="sheet">
  <header class="top-banner">治療に対する痛みや恐怖心を<br>できるだけ取り除きながら診療を行います</header>

  <section class="brand">
    <div class="brand-mark" aria-hidden="true"></div>
    <div class="brand-name">楠が浜台歯科クリニック</div>
    <div class="brand-en">Kusunohamadai Dental Clinic</div>
    <div class="cert">
      <div class="cert-label">近隣保育園<br>小学校・中学校<br>認定医</div>
      <div class="cert-seal" aria-hidden="true"></div>
    </div>
  </section>

  <section class="lower">
    <article class="card mothers">
      <span class="icon" aria-hidden="true"></span>
      <h2>お母さんに優しい<br>マザーズデー</h2>
      <p>当院では「マザーズデイ診療」を設けており、小さなお子さん連れでもお気軽にご来院いただけます。お母さんが診療中は、キッズスペースでスタッフがお子さんをお預かりします。お子さまも安心して待つことができます。対象年齢は1歳からです。（1歳未満のお子さまもご相談ください）お気軽にご相談ください。</p>
      <div class="days"><small>実施日</small><strong>月・火・金 9:00-12:00</strong></div>
    </article>

    <article class="card painless">
      <span class="icon" aria-hidden="true"></span>
      <h2>痛みが苦手な方でも<br>安心できる治療</h2>
      <p>当院では無針注射を用いるなど、痛みが軽減するよう努力しています。不安や緊張をほぐしながら、安心して治療を受けていただけるよう心がけています。</p>
    </article>

    <div class="postnatal">
      <div class="lead">産後健診も受付中！</div>
      <div class="sub">相模原市乳幼児健診担当医在中</div>
    </div>

    <div class="director-photo" role="img" aria-label="院長の写真"></div>
    <div class="director-caption">院長 森田 健一</div>

    <table class="hours">
      <thead><tr><th></th><th>月</th><th>火</th><th>水</th><th>木</th><th>金</th><th>土</th><th>日</th><th>祝</th></tr></thead>
      <tbody>
        <tr><th>9:00-12:00</th><td>○</td><td>○</td><td>○</td><td>○</td><td>○</td><td>△</td><td>−</td><td>−</td></tr>
        <tr><th>14:00-18:00</th><td>○</td><td>○</td><td>▲</td><td>○</td><td>○</td><td>△</td><td>−</td><td>−</td></tr>
      </tbody>
    </table>
    <p class="hours-note">▲…14:00-18:00　△…9:00-18:00（休憩なしで診療）</p>
  </section>

  <footer class="footer">
    <div class="tel">
      <svg width="26" height="26" viewBox="0 0 24 24" aria-hidden="true"><path fill="#fff" d="M6.6 10.8a15.1 15.1 0 0 0 6.6 6.6l2.2-2.2c.3-.3.7-.4 1-.2 1.1.4 2.3.6 3.6.6.6 0 1 .4 1 1V20c0 .6-.4 1-1 1A17 17 0 0 1 3 4c0-.6.4-1 1-1h3.5c.6 0 1 .4 1 1 0 1.3.2 2.5.6 3.6.1.3 0 .7-.2 1z"/></svg>
      042-700-3182
    </div>
    <div class="note">初めての方はweb予約フォームもご利用ください</div>
    <div class="web">
      <svg width="22" height="22" viewBox="0 0 24 24" aria-hidden="true"><path fill="#fff" d="M12 3 2 12h3v8h5v-5h4v5h5v-8h3z"/></svg>
      https://www.kusunohama-dc.jp
    </div>
  </footer>
</div>
</body>
</html>
```